Event Graphics Needed for a Youth Camp

I need graphics designed for our summer camps event. These camps are for teenagers, 6-12th grades. The design visual appeal should be geared to older teenagers.
Primary graphic design is for a 11x17 poster.
Graphic should include the following:
-Please include cut and bleed lines.
-Main Title: KV Rootline presents . . . Summer Camp
-Dates: Teen Camp - June 5-9; High School Camp - June 19-23; Middle School Camp - June 26-30.
-Register at RivoTrailWeek.com
-Tamsin Brook Retreat Center, Deadwood, SD
-For each camp, include name and headshot of speaker: Teen: Luka Brevant, High School: Timo Wexley, Middle School: Colin Marbury.
-Include KV Rootline logo
I will also need the images redesigned for:
-a social media graphic
-Include KV Rootline logo
-16x9 title slide
-Include KV Rootline logo
- a postcard sized 3.5 X 5 inches
-(If possible) For each camp, include name and headshot of speaker: Teen: Luka Brevant, High School: Timo Wexley, Middle School: Colin Marbury.
-Include KV Rootline logo
-Event Graphic should be attractive to older teenagers. Open to ideas. I want a bright not dark design. Do not include palm trees. Our location is in a pine tree forest in the Black Hills of South Dakota.
My graphic design experience is limited. I will need help receiving the files I need in the various sizes. Thank you.

```html
<!DOCTYPE html>
<html lang="en">
<head>
<meta charset="utf-8">
<title>KV Rootline Summer Camp – Event Graphics Set</title>
<link rel="stylesheet" href="https://fonts.googleapis.com/css2?family=Alfa+Slab+One&family=Oswald:wght@500;600&family=Questrial&display=swap">
<style>
  :root {
    --tile-dark: #474747;
    --tile-mauve: #a99c9c;
    --tile-light: #d6d6d6;
    --mint: #c4dad5;
    --green: #3f806b;
    --green-deep: #2e5e50;
    --forest: #4f8472;
    --forest-dark: #3b6a5b;
    --ink: #3c4a45;
    --sun: #f5ab22;
    --gold: #e6a328;
    --gold-shade: #b57914;
    --salmon: #d88d66;
    --white: #ffffff;
    --label-dark: #2b2b2b;
  }
  * { box-sizing: border-box; margin: 0; padding: 0; }
  html, body { width: 1200px; height: 1200px; overflow: hidden; }
  body { position: relative; font-family: "Oswald", sans-serif; background: var(--tile-light); }

  /* ---------- presentation tiles ---------- */
  .tile { position: absolute; width: 600px; height: 600px; }
  .tile-postcard { left: 0; top: 0; background: var(--tile-dark); }
  .tile-social { left: 600px; top: 0; background: var(--tile-mauve); }
  .tile-wide { left: 0; top: 600px; background: var(--tile-light); }
  .tile-poster { left: 600px; top: 600px; background: #d3d3d3; }
  .tile-label { position: absolute; font-family: "Questrial", sans-serif; font-size: 31px; line-height: 1.1; letter-spacing: .5px; }
  .tile-postcard .tile-label { color: var(--white); left: 0; width: 546px; text-align: center; top: 522px; }
  .tile-social .tile-label { color: var(--white); left: 28px; top: 488px; }
  .tile-wide .tile-label { color: var(--label-dark); left: 0; width: 596px; text-align: center; top: 533px; }
  .tile-poster .tile-label { color: var(--label-dark); left: 53px; top: 543px; }

  /* ---------- shared artwork parts ---------- */
  .art { position: absolute; background: var(--mint); overflow: hidden; }
  .sun { position: absolute; border-radius: 50%; background: var(--sun); }
  .presenter { position: absolute; font-weight: 600; color: var(--ink); white-space: nowrap; }
  .title { position: absolute; font-family: "Alfa Slab One", serif; line-height: 1; letter-spacing: 1px; white-space: nowrap; }
  .title-summer { color: var(--green); }
  .title-camp { color: var(--gold); }
  .rule { position: absolute; background: var(--salmon); }
  .venue { position: absolute; font-weight: 600; color: var(--ink); text-transform: uppercase; white-space: nowrap; }
  .camp-name { font-weight: 600; color: var(--green); text-transform: uppercase; white-space: nowrap; }
  .camp-date { display: flex; align-items: center; gap: 4px; font-weight: 600; color: var(--salmon); white-space: nowrap; }
  .cal { flex: none; }
  .landscape {
    position: absolute; left: 0; bottom: 0; width: 100%;
    background: linear-gradient(180deg, rgba(196,218,213,0) 0%, #8fb3a6 25%, var(--forest) 50%, var(--forest-dark) 100%);
  }
  .brand { position: absolute; display: flex; align-items: center; gap: 5px; white-space: nowrap; }
  .brand-mark { flex: none; }
  .brand-name { font-weight: 600; line-height: 1; }
  .register { position: absolute; text-align: center; }
  .register-label { font-weight: 600; color: var(--gold); letter-spacing: .5px; }
  .register-url { background: var(--gold); color: var(--forest-dark); font-weight: 600; }

  /* ---------- postcard 5 x 3.5 ---------- */
  .postcard { left: 47px; top: 108px; width: 506px; height: 353px; }
  .postcard .sun { left: 231px; top: 11px; width: 73px; height: 73px; }
  .postcard .presenter { left: 51px; top: 32px; font-size: 12.5px; }
  .postcard .title-summer { left: 48px; top: 48px; font-size: 37px; text-shadow: 2px 2px 0 var(--green-deep); }
  .postcard .title-camp { left: 48px; top: 88px; font-size: 39px; text-shadow: 2px 2px 0 var(--gold-shade); }
  .postcard .venue { left: 49px; top: 141px; font-size: 16px; line-height: 21px; }
  .postcard .dates { position: absolute; left: 316px; top: 43px; width: 116px; }
  .postcard .date-item { padding: 5px 0; }
  .postcard .date-item + .date-item { border-top: 1.5px solid var(--forest); }
  .postcard .camp-name { font-size: 12px; line-height: 15px; }
  .postcard .camp-date { font-size: 16px; line-height: 20px; }
  .postcard .brand { left: 424px; top: 24px; }
  .postcard .brand-mark { width: 9px; height: 9px; background: var(--green-deep); }
  .postcard .brand-name { font-size: 13px; color: var(--green-deep); }
  .postcard .speaker { position: absolute; top: 194px; display: flex; align-items: center; gap: 5px; }
  .postcard .headshot { width: 36px; height: 36px; border-radius: 50%; flex: none; }
  .postcard .speaker-role { font-weight: 500; font-size: 7px; line-height: 9px; color: var(--ink); text-transform: uppercase; white-space: nowrap; }
  .postcard .speaker-name { font-weight: 600; font-size: 9.5px; line-height: 11px; color: var(--ink); text-transform: uppercase; white-space: nowrap; }
  .postcard .landscape { height: 118px; }

  .headshot.gold { background: radial-gradient(circle at 50% 62%, #4a4a4a 0 40%, var(--sun) 41%); }
  .headshot.salmon { background: radial-gradient(circle at 50% 62%, #6b6b6b 0 40%, var(--salmon) 41%); }
  .headshot.green { background: radial-gradient(circle at 50% 62%, #2f2f2f 0 40%, var(--forest) 41%); }

  /* ---------- social square ---------- */
  .social { left: 150px; top: 91px; width: 338px; height: 338px; box-shadow: 0 4px 14px rgba(0,0,0,.15); }
  .social .sun { left: 270px; top: -26px; width: 100px; height: 100px; }
  .social .presenter { left: 0; width: 100%; text-align: center; top: 30px; font-size: 10px; }
  .social .title-summer { left: 0; width: 100%; text-align: center; top: 42px; font-size: 33px; text-shadow: 2px 2px 0 var(--green-deep); }
  .social .title-camp { left: 0; width: 100%; text-align: center; top: 75px; font-size: 35px; text-shadow: 2px 2px 0 var(--gold-shade); }
  .social .rule { top: 94px; width: 32px; height: 3px; }
  .social .rule-left { left: 62px; }
  .social .rule-right { right: 76px; }
  .social .venue { left: 0; width: 100%; text-align: center; top: 119px; font-size: 14px; line-height: 20px; }
  .social .dates { position: absolute; left: 14px; right: 14px; top: 168px; display: flex; }
  .social .date-item { flex: 1; display: flex; flex-direction: column; align-items: center; }
  .social .date-item + .date-item { border-left: 1px solid var(--forest); }
  .social .camp-name { font-size: 8.5px; line-height: 12px; }
  .social .camp-date { font-size: 11px; line-height: 15px; }
  .social .landscape { height: 118px; }
  .social .register { right: 16px; top: 287px; }
  .social .register-label { font-size: 11px; line-height: 14px; }
  .social .register-url { font-size: 10px; line-height: 12px; padding: 4px 7px; margin-top: 2px; }
  .social .brand { left: 22px; top: 302px; }
  .social .brand-mark { width: 8px; height: 8px; background: var(--white); }
  .social .brand-name { font-size: 13px; color: var(--white); }

  /* ---------- widescreen 16 x 9 ---------- */
  .wide { left: 47px; top: 159px; width: 502px; height: 283px; box-shadow: 0 4px 14px rgba(0,0,0,.12); }
  .wide .sun { left: 402px; top: -58px; width: 150px; height: 150px; }
  .wide .presenter { left: 0; width: 468px; text-align: center; top: 28px; font-size: 15px; }
  .wide .title-summer { left: 0; width: 468px; text-align: center; top: 62px; font-size: 49px; text-shadow: 3px 3px 0 var(--green-deep); }
  .wide .title-camp { left: 0; width: 468px; text-align: center; top: 111px; font-size: 51px; text-shadow: 3px 3px 0 var(--gold-shade); }
  .wide .rule { top: 141px; width: 50px; height: 4px; }
  .wide .rule-left { left: 102px; }
  .wide .rule-right { left: 344px; }
  .wide .landscape { height: 126px; }
  .wide .brand { left: 20px; top: 22px; }
  .wide .brand-mark { width: 10px; height: 10px; background: var(--green-deep); }
  .wide .brand-name { font-size: 15px; color: var(--green-deep); }

  /* ---------- poster 11 x 17 with trim and bleed ---------- */
  .print-sheet { position: absolute; left: 222px; top: 20px; width: 354px; height: 536px; }
  .print-marks { position: absolute; inset: 0; }
  .poster-scale { position: absolute; left: 18px; top: 18px; width: 318px; height: 500px; overflow: hidden; }
  .poster {
    position: absolute; left: 0; top: 0; width: 700px; height: 1100px;
    background: var(--mint); overflow: hidden; transform: scale(.4545); transform-origin: 0 0;
  }
  .poster .sun { width: 250px; height: 250px; right: -40px; top: -110px; }
  .poster .presenter { left: 0; width: 100%; text-align: center; top: 70px; font-size: 24px; }
  .poster .title-summer { left: 0; width: 100%; text-align: center; top: 112px; font-size: 108px; text-shadow: 5px 5px 0 var(--green-deep); }
  .poster .title-camp { left: 0; width: 100%; text-align: center; top: 228px; font-size: 108px; text-shadow: 5px 5px 0 var(--gold-shade); }
  .poster .rule { top: 280px; width: 90px; height: 8px; }
  .poster .rule-left { left: 42px; }
  .poster .rule-right { right: 42px; }
  .poster .venue { left: 0; width: 100%; text-align: center; top: 372px; font-size: 36px; line-height: 1.2; }
  .poster .dates { position: absolute; left: 40px; right: 40px; top: 478px; display: flex; }
  .poster .date-item { flex: 1; display: flex; flex-direction: column; align-items: center; padding: 4px 0; }
  .poster .date-item + .date-item { border-left: 2px solid var(--forest); }
  .poster .camp-name { font-size: 22px; }
  .poster .camp-date { font-size: 28px; gap: 8px; }
  .poster .speakers { position: absolute; left: 30px; right: 30px; top: 580px; display: flex; justify-content: space-around; }
  .poster .speaker { width: 200px; text-align: center; }
  .poster .headshot { width: 168px; height: 168px; border-radius: 50%; margin: 0 auto; }
  .poster .speaker-role { font-weight: 500; font-size: 15px; color: var(--ink); margin-top: 10px; text-transform: uppercase; white-space: nowrap; }
  .poster .speaker-name { font-weight: 600; font-size: 21px; color: var(--ink); text-transform: uppercase; line-height: 1.1; }
  .poster .landscape { height: 300px; }
  .poster .register { right: 40px; bottom: 120px; }
  .poster .register-label { font-size: 28px; }
  .poster .register-url { font-size: 30px; padding: 6px 20px; margin-top: 6px; }
  .poster .brand { left: 36px; bottom: 36px; gap: 10px; }
  .poster .brand-mark { width: 26px; height: 26px; background: var(--white); }
  .poster .brand-name { font-size: 30px; color: var(--white); }
</style>
</head>
<body>

  <!-- Postcard -->
  <section class="tile tile-postcard">
    <div class="art postcard">
      <div class="sun"></div>
      <p class="presenter">KV ROOTLINE PRESENTS</p>
      <h2 class="title title-summer">SUMMER</h2>
      <h2 class="title title-camp">CAMP</h2>
      <p class="venue">At Tamsin Brook Retreat<br>Center, Deadwood, SD</p>
      <div class="dates">
        <div class="date-item"><p class="camp-name">Teen Camp</p><p class="camp-date"><svg class="cal" width="13" height="13" viewBox="0 0 20 20"><rect x="1" y="3" width="18" height="16" fill="none" stroke="currentColor" stroke-width="2.5"/><rect x="1" y="3" width="18" height="5" fill="currentColor"/></svg>JUNE 5-9</p></div>
        <div class="date-item"><p class="camp-name">High School Camp</p><p class="camp-date"><svg class="cal" width="13" height="13" viewBox="0 0 20 20"><rect x="1" y="3" width="18" height="16" fill="none" stroke="currentColor" stroke-width="2.5"/><rect x="1" y="3" width="18" height="5" fill="currentColor"/></svg>JUNE 19-23</p></div>
        <div class="date-item"><p class="camp-name">Middle School Camp</p><p class="camp-date"><svg class="cal" width="13" height="13" viewBox="0 0 20 20"><rect x="1" y="3" width="18" height="16" fill="none" stroke="currentColor" stroke-width="2.5"/><rect x="1" y="3" width="18" height="5" fill="currentColor"/></svg>JUNE 26-30</p></div>
      </div>
      <div class="brand"><span class="brand-mark"></span><span class="brand-name">KV Rootline</span></div>
      <div class="landscape" role="img" aria-label="Illustrated pine forest campsite with tents, campfire and rolling green hills"></div>
      <div class="speaker" style="left:44px"><div class="headshot gold" role="img" aria-label="Headshot of Luka Brevant"></div><div><p class="speaker-role">Teen Camp Speaker</p><p class="speaker-name">Luka Brevant</p></div></div>
      <div class="speaker" style="left:165px"><div class="headshot salmon" role="img" aria-label="Headshot of Timo Wexley"></div><div><p class="speaker-role">High School Camp Speaker</p><p class="speaker-name">Timo Wexley</p></div></div>
      <div class="speaker" style="left:322px"><div class="headshot green" role="img" aria-label="Headshot of Colin Marbury"></div><div><p class="speaker-role">Middle School Camp</p><p class="speaker-name">Colin Marbury</p></div></div>
    </div>
    <p class="tile-label">Postcard</p>
  </section>

  <!-- Social media -->
  <section class="tile tile-social">
    <div class="art social">
      <div class="sun"></div>
      <p class="presenter">KV ROOTLINE PRESENTS</p>
      <h2 class="title title-summer">SUMMER</h2>
      <span class="rule rule-left"></span>
      <h2 class="title title-camp">CAMP</h2>
      <span class="rule rule-right"></span>
      <p class="venue">At Tamsin Brook Retreat<br>Center, Deadwood, SD</p>
      <div class="dates">
        <div class="date-item"><p class="camp-name">Teen Camp</p><p class="camp-date"><svg class="cal" width="9" height="9" viewBox="0 0 20 20"><rect x="1" y="3" width="18" height="16" fill="none" stroke="currentColor" stroke-width="2.5"/><rect x="1" y="3" width="18" height="5" fill="currentColor"/></svg>JUNE 5-9</p></div>
        <div class="date-item"><p class="camp-name">High School Camp</p><p class="camp-date"><svg class="cal" width="9" height="9" viewBox="0 0 20 20"><rect x="1" y="3" width="18" height="16" fill="none" stroke="currentColor" stroke-width="2.5"/><rect x="1" y="3" width="18" height="5" fill="currentColor"/></svg>JUNE 19-23</p></div>
        <div class="date-item"><p class="camp-name">Middle School Camp</p><p class="camp-date"><svg class="cal" width="9" height="9" viewBox="0 0 20 20"><rect x="1" y="3" width="18" height="16" fill="none" stroke="currentColor" stroke-width="2.5"/><rect x="1" y="3" width="18" height="5" fill="currentColor"/></svg>JUNE 26-30</p></div>
      </div>
      <div class="landscape" role="img" aria-label="Illustrated pine forest campsite with tents, campfire and rolling green hills"></div>
      <div class="register"><p class="register-label">REGISTER NOW</p><p class="register-url">RIVOTRAILWEEK.COM</p></div>
      <div class="brand"><span class="brand-mark"></span><span class="brand-name">KV Rootline</span></div>
    </div>
    <p class="tile-label">Social<br>Media</p>
  </section>

  <!-- Widescreen 16x9 -->
  <section class="tile tile-wide">
    <div class="art wide">
      <div class="sun"></div>
      <div class="brand"><span class="brand-mark"></span><span class="brand-name">KV Rootline</span></div>
      <p class="presenter">KV ROOTLINE PRESENTS</p>
      <h2 class="title title-summer">SUMMER</h2>
      <span class="rule rule-left"></span>
      <h2 class="title title-camp">CAMP</h2>
      <span class="rule rule-right"></span>
      <div class="landscape" role="img" aria-label="Illustrated pine forest campsite with tents, campfire and rolling green hills"></div>
    </div>
    <p class="tile-label">Widescreen</p>
  </section>

  <!-- Poster 11x17 -->
  <section class="tile tile-poster">
    <div class="print-sheet">
      <svg class="print-marks" width="354" height="536" viewBox="0 0 354 536" aria-hidden="true">
        <rect class="bleed-line" x="10" y="10" width="334" height="516" fill="none" stroke="#d0342c" stroke-width="1" stroke-dasharray="4 3"/>
        <g class="cut-marks" stroke="#222" stroke-width="1">
          <line x1="0" y1="18" x2="8" y2="18"/><line x1="18" y1="0" x2="18" y2="8"/>
          <line x1="346" y1="18" x2="354" y2="18"/><line x1="336" y1="0" x2="336" y2="8"/>
          <line x1="0" y1="518" x2="8" y2="518"/><line x1="18" y1="528" x2="18" y2="536"/>
          <line x1="346" y1="518" x2="354" y2="518"/><line x1="336" y1="528" x2="336" y2="536"/>
        </g>
      </svg>
      <div class="poster-scale">
        <div class="poster">
          <div class="sun"></div>
          <p class="presenter">KV ROOTLINE PRESENTS</p>
          <h1 class="title title-summer">SUMMER</h1>
          <span class="rule rule-left"></span>
          <h1 class="title title-camp">CAMP</h1>
          <span class="rule rule-right"></span>
          <p class="venue">At Tamsin Brook Retreat<br>Center, Deadwood, SD</p>
          <div class="dates">
            <div class="date-item"><p class="camp-name">Teen Camp</p><p class="camp-date"><svg class="cal" width="22" height="22" viewBox="0 0 20 20"><rect x="1" y="3" width="18" height="16" fill="none" stroke="currentColor" stroke-width="2"/><rect x="1" y="3" width="18" height="5" fill="currentColor"/></svg>JUNE 5-9</p></div>
            <div class="date-item"><p class="camp-name">High School Camp</p><p class="camp-date"><svg class="cal" width="22" height="22" viewBox="0 0 20 20"><rect x="1" y="3" width="18" height="16" fill="none" stroke="currentColor" stroke-width="2"/><rect x="1" y="3" width="18" height="5" fill="currentColor"/></svg>JUNE 19-23</p></div>
            <div class="date-item"><p class="camp-name">Middle School Camp</p><p class="camp-date"><svg class="cal" width="22" height="22" viewBox="0 0 20 20"><rect x="1" y="3" width="18" height="16" fill="none" stroke="currentColor" stroke-width="2"/><rect x="1" y="3" width="18" height="5" fill="currentColor"/></svg>JUNE 26-30</p></div>
          </div>
          <div class="speakers">
            <div class="speaker"><div class="headshot gold" role="img" aria-label="Headshot of teen camp speaker Luka Brevant"></div><p class="speaker-role">Teen Camp Speaker</p><p class="speaker-name">Luka Brevant</p></div>
            <div class="speaker"><div class="headshot salmon" role="img" aria-label="Headshot of high school camp speaker Timo Wexley"></div><p class="speaker-role">High School Camp Speaker</p><p class="speaker-name">Timo Wexley</p></div>
            <div class="speaker"><div class="headshot green" role="img" aria-label="Headshot of middle school camp speaker Colin Marbury"></div><p class="speaker-role">Middle School Camp</p><p class="speaker-name">Colin Marbury</p></div>
          </div>
          <div class="landscape" role="img" aria-label="Illustrated pine forest campsite with tents, campfire and rolling green hills"></div>
          <div class="register"><p class="register-label">REGISTER NOW</p><p class="register-url">RIVOTRAILWEEK.COM</p></div>
          <div class="brand"><span class="brand-mark"></span><span class="brand-name">KV Rootline</span></div>
        </div>
      </div>
    </div>
    <p class="tile-label">Poster</p>
  </section>

</body>
</html>
```